Kelvara Learning Australia - Course Brochure Design

Kelvara Learning Australia is a Private Register Training Organisation that delivery accredited training courses to students. These courses are delivery via face to face training and distance education (e.g. elearning).

We are looking to get a template designed via adobe in design that we can use for each of our courses and list the information relevant for each one.

It will need to be around 3 - 4 pages long to be able to fit the information required into the brochure, i have attached some example of other providers course information sheets.

From the examples you'll be able to see that most of the information will remained the same until it gets to the course structure.

I would like it to be kept within our current theme, we are in the middle of upgrading our new website and look (www.kelvara.com.au/drupal).

I look forward to see what you all come back with.
Updates

Project Deadline Extended
Reason: Hi everyone, Thanks for submitting your design, I have extended the deadline due to not many designs have been submitted. I will be review and providing feedback on the designed submitted this week and will provide some more information based off the work and direction of the designs submitted. Thanks, Pedro.

Target Market(s)

our target market is business and individuals who would like to undergo training course. This brochure needs to display the require information.

Industry/Entity Type

Education

Requirements
Must have
• The brochure must have a front page with a design to list our company logo and information and the course title.

A call to action must be on every page, e.g. footer to enrol now call kelvra on 1800 392 058 or visit www.kelvara.com.au

Nice to have
• Some picture to fill the pages would add a nice look

```html
<!DOCTYPE html>
<html lang="en">
<head>
<meta charset="utf-8">
<title>Kelvara Learning Australia – Course Brochure Spread</title>
<link href="https://fonts.googleapis.com/css2?family=Open+Sans:wght@400;600;700&display=swap" rel="stylesheet">
<style>
  :root {
    --backdrop: #3b3b3b;
    --paper: #ffffff;
    --brand-red: #8a1a12;
    --ink: #4a4a4a;
    --ink-soft: #6d6d6d;
    --rule: #d9d9d9;
    --panel-grey: #5f6062;
    --panel-text: #e6e6e6;
  }
  * { box-sizing: border-box; margin: 0; padding: 0; }
  html, body { width: 1200px; height: 900px; overflow: hidden; }
  body {
    background: var(--backdrop);
    font-family: "Open Sans", Arial, sans-serif;
    color: var(--ink);
    position: relative;
  }
  .spread { position: absolute; left: 40px; top: 40px; width: 1120px; height: 820px; }
  .page { position: absolute; top: 0; width: 560px; height: 820px; overflow: hidden; }
  .page--inside { left: 0; background: var(--paper); }
  .page--cover { left: 560px; background: #dfe4e8; }

  /* inside page */
  .header-band { position: absolute; left: 220px; top: 0; width: 340px; height: 26px; background: var(--brand-red); }
  .running-head {
    position: absolute; left: 12px; top: 28px;
    font-size: 9px; font-weight: 600; color: var(--brand-red);
    padding-left: 10px; border-left: 4px solid var(--brand-red); line-height: 12px;
  }
  .feature-photo {
    position: absolute; left: 24px; top: 62px; width: 316px; height: 130px;
    background: linear-gradient(100deg, #c9cfd6 0%, #e8ebee 40%, #b9a59a 65%, #dcdfe3 100%);
  }
  .course-table { position: absolute; left: 24px; top: 206px; width: 512px; border-collapse: collapse; }
  .course-table td {
    font-size: 8px; line-height: 10.5px; color: var(--ink-soft);
    vertical-align: top; padding: 9px 4px 9px; border-bottom: 1px solid var(--rule);
  }
  .course-table td.code { width: 94px; color: var(--ink); padding-left: 6px; }
  .course-table td.unit { width: 120px; }
  .course-table tr:last-child td { border-bottom: 2px solid var(--brand-red); }
  .section-heading {
    position: absolute; left: 24px; top: 622px;
    font-size: 10px; font-weight: 700; color: var(--brand-red); letter-spacing: 0.2px;
  }
  .section-copy {
    position: absolute; left: 24px; top: 644px; width: 512px;
    font-size: 8px; line-height: 12px; color: var(--ink-soft);
  }
  .footer-rule { position: absolute; left: 24px; right: 0; top: 770px; border-top: 1px solid var(--rule); }
  .footer-block { position: absolute; left: 0; top: 776px; width: 32px; height: 44px; background: var(--brand-red); }
  .call-to-action {
    position: absolute; left: 40px; right: 0; top: 790px; text-align: center;
    font-size: 11px; color: var(--ink-soft);
  }
  .call-to-action strong { color: var(--ink); font-weight: 700; }

  /* cover page */
  .cover-photo {
    position: absolute; inset: 0;
    background:
      radial-gradient(ellipse 170px 240px at 345px 260px, #c9d2dc 0%, rgba(201,210,220,0) 100%),
      linear-gradient(90deg, #9aa1a8 0%, #d5dbe1 30%, #eef1f4 60%, #f4f6f8 100%);
  }
  .brand-name {
    position: absolute; right: 36px; top: 52px;
    display: flex; align-items: center; gap: 8px;
    font-size: 26px; font-weight: 700; color: var(--brand-red);
  }
  .brand-name .mark { width: 12px; height: 12px; background: var(--brand-red); }
  .cover-panel { position: absolute; left: 0; top: 0; width: 560px; height: 820px; }
  .course-title {
    position: absolute; left: 26px; top: 640px;
    font-size: 34px; font-weight: 400; color: #ffffff;
  }
  .cover-intro {
    position: absolute; left: 26px; top: 696px; width: 330px;
    font-size: 7px; line-height: 10px; color: var(--panel-text);
  }
  .cover-cta {
    position: absolute; left: 26px; right: 26px; top: 790px;
    font-size: 11px; color: var(--panel-text);
  }
  .cover-cta strong { color: #ffffff; font-weight: 700; }
</style>
</head>
<body>
<div class="spread">

  <section class="page page--inside">
    <div class="header-band"></div>
    <div class="running-head">Quidit endes exeris de explita eum</div>
    <div class="feature-photo" role="img" aria-label="Photo of a trainer helping learners at computers in a classroom"></div>

    <table class="course-table">
      <tr><td class="code">00000</td><td class="unit">Ct is aut ut denimpus aliatibus sa simag</td><td>Tem quo moluptatius dis doluptate nihitis volo molor aut endiatusa maximus orporro volorro nimenimo unt omnis imenden eosam voluptatis</td></tr>
      <tr><td class="code">00000</td><td class="unit">Penuptatem ipsam</td><td>Non reped quo ipsustrum ab id utempos essam dolor sequidunde cus dictum quo vel quiperror</td></tr>
      <tr><td class="code">00000</td><td class="unit">Maximus et odigentur. Et am nimus.</td><td>Solum que et repro maximporum quo eos natiori tsuntem. Non pla quid unt doluessit elluptur cuptaque beritae vel lam quam aut enis et</td></tr>
      <tr><td class="code">00000</td><td class="unit">Veliquamus sun expli</td><td>Genimus as maxim que pa nimin nectotae nonectur</td></tr>
      <tr><td class="code">00000</td><td class="unit">Fugit maximus ne quam aut que nort nullaho rpcres</td><td>Volorem illessit scimpe pratur ut ut ventis et illessa aut nis que lates. Ut lam, occuptas is ex iliandus sit volectius, soluptatus autibo volorito molluptae</td></tr>
      <tr><td class="code">00000</td><td class="unit">Quatem peribus ea comni simpore sumen</td><td>Quoditium reptatempos dis utem quaet velessi monduae ist commnimodo qui quiat mo ex et dolorum et landicae nim cusdae prae doluptat il dignihit aut alis cute rem et ende es maionepudae dolenim agnate quae nati con rere, quiae nis aborepra nonsequi doluptis dolore dolent autre</td></tr>
      <tr><td class="code">00000</td><td class="unit">Officia cor maximin ida nulpa volor rem</td><td>Ihitia vendelli gentinimpel quit ut aliquis moluptatiis est lab alliberendi dis ante magnisitam aut harias quo excestur itae net quia vellab ipit rest laceasp iandant haut edit</td></tr>
      <tr><td class="code">00000</td><td class="unit">Ateunnet ut essitat.</td><td>Parunt, sequam non es aliat elitas quidelist endiaessed etur magnimusam la nequi ducieup aniatus volunt none dolupta nam, ipsum verbus maximen totati</td></tr>
    </table>

    <h2 class="section-heading">AUDAM INCIPITIORE IM QUI OPTUR AUT FUGA</h2>
    <p class="section-copy">Quo reptas autebius sunt platus. Lessequae pitiae troques molenequa ommoditatis, volo et am, offic iet latatem autetibeate re optat experis ommolut luptur soluptia tiumtume et, sum ipis si nonsequo ollorepu si ise pre volorpos conseque ilessam ea nonsequ eeribus ommolu platibusda consequa beaurum renust et renatur? Mus est cum enitessumi nam, lessi ped mo tem est, suntemp reiepta quo quam natum et volorpit eata int audam incipitiore im qui optur aut fuga. Nam rem sit etur sectus qui torit volorem receris invoatnet susatit et dolupta fuga, ut et susa delis eum, conseque ipsamen entio. Apid quam, et doluptaque ulit hiatet aut lab ipsam, simba errus voluptia epercidelique icid quas dem fugiat ilum.</p>

    <div class="footer-rule"></div>
    <div class="footer-block"></div>
    <p class="call-to-action">To enrol now, call Kelvara on <strong>1800 392 058</strong> or visit <strong>www.kelvara.com.au</strong></p>
  </section>

  <section class="page page--cover">
    <div class="cover-photo" role="img" aria-label="Photo of a smiling professional in an office with a colleague in the background"></div>
    <div class="brand-name"><span class="mark"></span>Kelvara</div>
    <svg class="cover-panel" viewBox="0 0 560 820" aria-hidden="true">
      <polygon points="0,610 560,500 560,820 0,820" fill="var(--panel-grey)"/>
    </svg>
    <h1 class="course-title">Id eumenietum alignam</h1>
    <p class="cover-intro">Iducimus alignam, omnistio ressit ut quiasi pelis quod quamusda aut earunt. Itaerum et eost qui que nem quis andandis ullibus. Nos ut exeruntotet doluptae dendi fugiat que lab ipsam et eaquat cum poria at erectendis. Im nimilit offic tem quam ut veleni, volupta que dollorest pelit aut dolupta.</p>
    <p class="cover-cta">To enrol now, call Kelvara on <strong>1800 392 058</strong> or visit <strong>www.kelvara.com.au</strong></p>
  </section>

</div>
</body>
</html>
```